Brona's Dwellings website

We need a simple website for our property investment business in the UK. We basically need our contact details and brief description.We have the company logo already done (via ArtVelo) so please use these:https://drive.google.com/drive/folders/1szJ3iRhelElZ40NIFT7w-c14MaY3Y_oV?usp=sharingYou could use some stock photos of UK houses for now.Let me know when to provide more detailed descriptions, etc

Coding

Coded - Design and coding required

Number of Pages Required

1 page

Colors

Designer to choose colors to be used in the design.

```html
<!DOCTYPE html>
<html lang="en">
<head>
<meta charset="utf-8">
<title>Brona's Dwellings</title>
<link rel="stylesheet" href="https://fonts.googleapis.com/css2?family=Montserrat:wght@400;600;700&family=Noto+Serif:ital,wght@0,400;1,400&display=swap">
<style>
:root{
  --ink:#212529;
  --muted:#6c757d;
  --grey-btn:#7b7b7b;
  --panel:#f7f7f7;
  --white:#ffffff;
  --social:#2a2f35;
}
*{box-sizing:border-box;margin:0;padding:0}
html,body{width:1200px;height:3601px;overflow:hidden;background:var(--white)}
body{position:relative;font-family:'Noto Serif',Georgia,serif;color:var(--ink)}
.abs{position:absolute}
.heading{font-family:'Montserrat',Arial,sans-serif;font-weight:700;text-transform:uppercase;text-align:center;left:0;width:1200px;font-size:34px;color:var(--ink)}
.subheading{font-style:italic;font-size:13px;color:var(--muted);text-align:center;left:0;width:1200px}

/* hero */
.hero{left:86px;top:86px;width:1007px;height:655px;overflow:hidden;
  background:linear-gradient(180deg,#6b7a8a 0%,#4c5a4a 40%,#3b4633 62%,#2c3a44 78%,#1f2a30 100%)}
.hero::after{content:"";position:absolute;inset:0;background:rgba(20,25,35,.35)}
.logo-box{left:88px;top:30px;width:113px;height:71px;background:rgba(40,45,55,.55);z-index:2;
  display:flex;align-items:center;justify-content:center;gap:6px;flex-direction:column}
.logo-box span{font-family:'Montserrat',Arial,sans-serif;font-weight:600;font-size:9px;letter-spacing:1.5px;color:#1b1f24;text-transform:uppercase;text-align:center;line-height:1.3}
.logo-box i{display:block;width:16px;height:16px;background:#1b1f24}
.nav{right:100px;top:56px;z-index:2;display:flex;gap:22px;font-family:'Montserrat',Arial,sans-serif;font-weight:600;font-size:11px;letter-spacing:1px;color:var(--white)}
.hero-lead{left:0;width:1007px;top:272px;text-align:center;font-style:italic;font-size:36px;color:var(--white);z-index:2}
.hero-title{left:0;width:1007px;top:335px;text-align:center;font-family:'Montserrat',Arial,sans-serif;font-weight:700;font-size:64px;color:var(--white);z-index:2;letter-spacing:-1px}
.btn{background:var(--grey-btn);color:var(--white);font-family:'Montserrat',Arial,sans-serif;font-weight:700;font-size:14px;text-transform:uppercase;display:flex;align-items:center;justify-content:center;border-radius:3px}
.hero .btn{z-index:2;top:452px;height:62px}

/* services */
.card{top:964px;width:282px;height:284px;background:var(--white);box-shadow:0 4px 12px rgba(0,0,0,.28);text-align:center;overflow:hidden}
.card .icon{width:120px;height:120px;border-radius:50%;background:var(--grey-btn);margin:13px auto 0;display:flex;align-items:center;justify-content:center}
.card h3{font-family:'Montserrat',Arial,sans-serif;font-weight:600;font-size:20px;line-height:24px;text-transform:uppercase;margin-top:14px}
.card p{font-size:12px;line-height:24px;color:var(--muted);padding:8px 16px 0;letter-spacing:-0.2px}

/* projects */
.projects-bg{left:86px;top:1334px;width:1007px;height:922px;background:var(--panel)}
.project{width:261px;height:281px;background:var(--white);text-align:center}
.project .photo{height:188px}
.project h4{font-family:'Montserrat',Arial,sans-serif;font-weight:600;font-size:20px;margin-top:22px}
.project small{display:block;font-style:italic;font-size:13px;color:var(--muted);margin-top:4px}

/* about */
.about-photo{left:205px;top:2479px;width:332px;height:239px;background:linear-gradient(180deg,#cfd6dc 0%,#6f5a48 35%,#3e5a2e 70%,#2c4a22 100%)}
.about-text{left:600px;top:2486px;width:420px;font-size:12px;line-height:24px;color:var(--muted);letter-spacing:-0.2px}
.about-text p{margin-bottom:14px}

/* contact */
.contact{left:86px;top:2814px;width:1007px;height:690px;background:#14181c;overflow:hidden}
.contact .scene{position:absolute;left:25px;top:0;width:957px;height:690px;
  background:linear-gradient(180deg,#55616e 0%,#3d4a3d 45%,#2c3828 65%,#27323a 82%,#1b242a 100%)}
.contact .scene::after{content:"";position:absolute;inset:0;background:rgba(20,25,35,.3)}
.contact .heading{top:104px;left:0;width:1007px;z-index:2;color:#1b1f24}
.info{top:237px;width:261px;height:69px;background:var(--white);text-align:center;z-index:2;overflow:hidden}
.info small{display:block;font-size:12px;margin-top:8px}
.info strong{display:block;font-family:'Montserrat',Arial,sans-serif;font-weight:600;font-size:19px;margin-top:10px;white-space:nowrap}
.info strong.mail{font-size:16px;letter-spacing:-0.2px}
.social{top:241px;width:37px;height:37px;border-radius:50%;background:var(--social);z-index:2;display:flex;align-items:center;justify-content:center}
.field{left:89px;width:402px;height:56px;background:var(--white);border-radius:3px;z-index:2;font-family:'Montserrat',Arial,sans-serif;font-size:12px;color:#c3c8ce;padding:17px 14px}
.message{left:514px;top:309px;width:404px;height:215px;background:var(--white);border-radius:3px;z-index:2;font-family:'Montserrat',Arial,sans-serif;font-size:12px;color:#c3c8ce;padding:17px 14px}
.contact .btn{left:417px;top:545px;width:172px;height:59px;z-index:2}

/* footer */
.footer-copy{left:288px;top:3537px;font-family:'Montserrat',Arial,sans-serif;font-size:11px;font-weight:600}
.footer-links{left:652px;top:3543px;display:flex;gap:9px;font-family:'Montserrat',Arial,sans-serif;font-size:11px;color:var(--muted)}
.footer-links span:nth-child(3){margin-left:12px}
.footer-links span:nth-child(4){margin-left:16px}
</style>
</head>
<body>

<header class="abs hero" role="img" aria-label="Photo of a white English cottage beside a river among autumn trees">
  <div class="abs logo-box"><i></i><span>Brona's Dwellings</span></div>
  <nav class="abs nav"><span>ABOUT</span><span>SERVICES</span><span>PROJECTS</span><span>CONTACT</span></nav>
  <div class="abs hero-lead">Brona's Dwellings</div>
  <h1 class="abs hero-title">IT'S NICE TO MEET YOU</h1>
  <div class="abs btn" style="left:356px;width:134px">Projects</div>
  <div class="abs btn" style="left:494px;width:154px">Learn More</div>
</header>

<h2 class="abs heading" style="top:827px">Services</h2>
<p class="abs subheading" style="top:881px">Lorem ipsum dolor sit amet consectetur.</p>

<div class="abs card" style="left:164px">
  <div class="icon"><svg width="56" height="52" viewBox="0 0 56 52"><path d="M28 4 3 26h8v22h13V34h8v14h13V26h8z" fill="#fff"/></svg></div>
  <h3>Service Type One</h3>
  <p>Lorem ipsum dolor sit amet, consectetur adipisicing elit. Minima maxime quam architecto quo inventore harum ex magni, dicta impedit.</p>
</div>
<div class="abs card" style="left:448px">
  <div class="icon"><svg width="40" height="56" viewBox="0 0 40 56"><rect x="6" y="2" width="28" height="52" fill="#fff"/><g fill="#7b7b7b"><rect x="12" y="8" width="5" height="6"/><rect x="23" y="8" width="5" height="6"/><rect x="12" y="20" width="5" height="6"/><rect x="23" y="20" width="5" height="6"/><rect x="12" y="32" width="5" height="6"/><rect x="23" y="32" width="5" height="6"/><rect x="16" y="44" width="8" height="10"/></g></svg></div>
  <h3>Service Type Two</h3>
  <p>Lorem ipsum dolor sit amet, consectetur adipisicing elit. Minima maxime quam architecto quo inventore harum ex magni, dicta impedit.</p>
</div>
<div class="abs card" style="left:733px">
  <div class="icon"><svg width="60" height="50" viewBox="0 0 60 50"><rect x="2" y="12" width="40" height="36" fill="#fff"/><rect x="24" y="2" width="18" height="12" fill="#fff"/><rect x="40" y="20" width="18" height="28" fill="#fff"/><g fill="#7b7b7b"><rect x="8" y="18" width="5" height="5"/><rect x="18" y="18" width="5" height="5"/><rect x="28" y="18" width="5" height="5"/><rect x="8" y="28" width="5" height="5"/><rect x="18" y="28" width="5" height="5"/><rect x="28" y="28" width="5" height="5"/><rect x="46" y="28" width="5" height="5"/><rect x="8" y="38" width="5" height="5"/><rect x="18" y="38" width="5" height="5"/><rect x="28" y="38" width="5" height="5"/><rect x="46" y="38" width="5" height="5"/></g></svg></div>
  <h3>Service Type Three</h3>
  <p>Lorem ipsum dolor sit amet, consectetur adipisicing elit. Minima maxime quam architecto quo inventore harum ex magni, dicta impedit.</p>
</div>

<section class="abs projects-bg"></section>
<h2 class="abs heading" style="top:1420px">Featured Projects</h2>
<p class="abs subheading" style="top:1474px">Lorem ipsum dolor sit amet consectetur.</p>

<div class="abs project" style="left:175px;top:1557px"><div class="photo" role="img" aria-label="Modern white apartment block with green balconies" style="background:linear-gradient(180deg,#3d6fc2 0%,#e6e6dc 40%,#b9c24a 75%,#7a8a3a 100%)"></div><h4>Project 1</h4><small>Category</small></div>
<div class="abs project" style="left:459px;top:1557px"><div class="photo" role="img" aria-label="Grand stone manor house with lawn" style="background:linear-gradient(180deg,#8fb0d8 0%,#9a9590 45%,#6f7d5a 75%,#4f7a2e 100%)"></div><h4>Project 2</h4><small>Category</small></div>
<div class="abs project" style="left:743px;top:1557px"><div class="photo" role="img" aria-label="White cottage reflected in a river" style="background:linear-gradient(180deg,#8fb2d6 0%,#4e6a32 40%,#d8d4cc 55%,#2c4a5a 100%)"></div><h4>Project 3</h4><small>Category</small></div>
<div class="abs project" style="left:175px;top:1864px"><div class="photo" role="img" aria-label="Thatched cottage behind a hedge" style="background:linear-gradient(180deg,#c9d3dc 0%,#5a6a3c 35%,#e8e2c4 65%,#4a5a22 100%)"></div><h4>Project 4</h4><small>Category</small></div>
<div class="abs project" style="left:459px;top:1864px"><div class="photo" role="img" aria-label="Thatched cottage with wooden fence" style="background:linear-gradient(180deg,#3e3a1e 0%,#8a7a50 40%,#d8cfa8 65%,#5a4a28 100%)"></div><h4>Project 5</h4><small>Category</small></div>
<div class="abs project" style="left:743px;top:1864px"><div class="photo" role="img" aria-label="Brick house behind a tall green hedge" style="background:linear-gradient(180deg,#cfd6dc 0%,#6f5a48 35%,#3e5a2e 65%,#2c4a22 100%)"></div><h4>Project 6</h4><small>Category</small></div>

<h2 class="abs heading" style="top:2343px">About</h2>
<p class="abs subheading" style="top:2397px">Lorem ipsum dolor sit amet consectetur.</p>
<div class="abs about-photo" role="img" aria-label="Brick house behind a tall green hedge"></div>
<div class="abs about-text">
  <p>Lorem ipsum dolor sit amet, consectetur adipisicing elit. Minima maxime quam architecto quo inventore harum ex magni, dicta impedit.</p>
  <p>Lorem ipsum dolor sit amet, consectetur adipisicing elit. Minima maxime quam architecto quo inventore harum ex magni, dicta impedit.</p>
  <p>Lorem ipsum dolor sit amet, consectetur adipisicing elit. Minima maxime quam architecto quo inventore harum ex magni, dicta impedit.</p>
  <p>Lorem ipsum dolor sit amet, consectetur adipisicing elit. Minima maxime quam architecto quo inventore harum ex magni, dicta impedit.</p>
</div>

<section class="abs contact">
  <div class="scene" role="img" aria-label="Darkened photo of a cottage beside a river among trees"></div>
  <h2 class="abs heading">Contact Us</h2>
  <div class="abs info" style="left:89px"><small>Call Us</small><strong>+1 5555 5555 55</strong></div>
  <div class="abs social" style="left:439px" aria-label="Share link"><svg width="16" height="16" viewBox="0 0 16 16"><circle cx="4" cy="8" r="2.2" fill="#fff"/><circle cx="12" cy="3.5" r="2.2" fill="#fff"/><circle cx="12" cy="12.5" r="2.2" fill="#fff"/><path d="M4 8 12 3.5M4 8l8 4.5" stroke="#fff" stroke-width="1.4"/></svg></div>
  <div class="abs social" style="left:485px" aria-label="Website link"><svg width="16" height="16" viewBox="0 0 16 16" fill="none" stroke="#fff" stroke-width="1.4"><circle cx="8" cy="8" r="6.3"/><ellipse cx="8" cy="8" rx="2.8" ry="6.3"/><path d="M1.7 8h12.6"/></svg></div>
  <div class="abs social" style="left:532px" aria-label="Message link"><svg width="16" height="16" viewBox="0 0 16 16"><path d="M2 3h12v8H7l-3 3v-3H2z" fill="#fff"/></svg></div>
  <div class="abs info" style="left:657px"><small>Mail Us</small><strong class="mail">mail@bronasdwellings.com</strong></div>
  <div class="abs field" style="top:309px">Your Name *</div>
  <div class="abs field" style="top:388px">Your Email *</div>
  <div class="abs field" style="top:467px">Your Phone *</div>
  <div class="abs message">Your Message *</div>
  <div class="abs btn">Send Message</div>
</section>

<footer>
  <div class="abs footer-copy">Copyright © Brona's Dwellings 2019</div>
  <div class="abs footer-links"><span>Privacy Policy</span><span>Terms of Use</span><span>About</span><span>Projects</span></div>
</footer>

</body>
</html>
```